Tamsin Crumbs business card design for pastry business

Hi! I need a fun, flirty business card to illustrate my business' cool and utterly delicious product! I'm picturing a cartoon 'me' - that is a young lady with a long blond ponytail, big blue eyes and smile, wearing a pink apron and with arms slightly bent and outstretched to the sides, palms up,balancing a slice of pie in one hand, and a cupcake on the other. Shades of soft yellow, pinks, mauves, and other pastels (perhaps?). Tamsin Crumbs is the name, I need a tagline to be written underneath - I was thinking 'Pies and Cakes' because it rhymes, but it's somewhat limiting since I do more than just those two items (there will be cinnamon rolls, cupcakes, muffins and scones, for example) I also want something that looks unique before you even read what's on it - so the paper and shape should be original as well.
Hi,
Thanks for all the submissions so far! I will respond to those individually, but wanted to post an update with more information on what I'm looking for.
I don't have a logo for those who requested it -
The 'cartoon' me I described - I would like it to look more 'fashion', less child-like - so the silhouette should look more proportionate to a woman's shape.
My hair is blond, but not yellow :) More of a dirty blond color.
Thank you again! Please ask me any other questions you have - the more info we exchange the closer we can get to the look I'm picturing!
Tamsin

```html
<!DOCTYPE html>
<html lang="en">
<head>
<meta charset="utf-8">
<title>Tamsin Crumbs — Business Card</title>
<link rel="stylesheet" href="https://fonts.googleapis.com/css2?family=Questrial&display=swap">
<style>
  :root {
    --page: #ffffff;
    --ink: #111111;
    --mauve: #a6969f;
    --cream: #f9f6c7;
    --title-grey: #9d959b;
    --text-grey: #8f8a8d;
    --rose: #e0606e;
    --figure-pink: #e8808c;
    --figure-blue: #cfe6f7;
    --figure-skin: #f4cfa0;
    --white: #ffffff;
  }
  * { box-sizing: border-box; margin: 0; padding: 0; }
  html, body {
    width: 1200px; height: 846px; overflow: hidden;
    background: var(--page);
    font-family: "Questrial", "Helvetica Neue", Arial, sans-serif;
  }
  .sheet { position: relative; width: 1200px; height: 846px; }

  .card {
    position: absolute; top: 142px; width: 313px; height: 513px;
    border: 2px solid var(--ink); border-radius: 48px; overflow: hidden;
  }
  .card--front { left: 149px; background: var(--mauve); color: var(--white); }
  .card--back  { left: 737px; background: var(--cream); color: var(--title-grey); }

  .brand { position: absolute; top: 42px; left: 0; right: 0; text-align: center; }
  .brand__name { font-size: 36px; font-weight: 400; letter-spacing: 0.5px; line-height: 38px; }
  .brand__tagline {
    display: flex; align-items: center; justify-content: center; gap: 10px;
    margin-top: 20px; font-size: 11px; line-height: 14px; letter-spacing: 1.6px;
  }
  .brand__tagline::before, .brand__tagline::after {
    content: ""; width: 38px; height: 1px; background: currentColor;
  }

  .figure {
    position: absolute; top: 146px; height: 352px;
    background: linear-gradient(180deg, var(--figure-skin) 0%, var(--figure-pink) 35%, var(--figure-blue) 70%, var(--figure-pink) 100%);
    opacity: 0.9;
  }
  .card--front .figure { left: 83px; width: 170px; border-radius: 60px 60px 20px 20px; }
  .card--back .figure  { left: -2px; width: 92px; border-radius: 0 46px 20px 0; }

  .contact {
    position: absolute; left: 101px; right: 6px; top: 240px;
    color: var(--text-grey); white-space: nowrap;
  }
  .contact__name { font-size: 18px; line-height: 20px; letter-spacing: 1.2px; margin-bottom: 18px; }
  .contact__row {
    display: flex; align-items: center; gap: 8px;
    font-size: 10.5px; letter-spacing: -0.1px; height: 30px; margin-bottom: 16px;
  }
  .contact__row svg { width: 28px; height: 28px; flex: none; }

  .side-label {
    position: absolute; top: 690px; width: 313px; text-align: center;
    font-size: 29px; letter-spacing: 4px; color: var(--ink);
  }
  .side-label--front { left: 149px; }
  .side-label--back  { left: 737px; }
</style>
</head>
<body>
<main class="sheet">
  <section class="card card--front" aria-label="Card front">
    <div class="brand">
      <h1 class="brand__name">Tamsin Crumbs</h1>
      <p class="brand__tagline">TREATS AND CAKES</p>
    </div>
    <div class="figure" role="img" aria-label="Illustration of a baker in a pink apron holding a tray of cupcakes"></div>
  </section>

  <section class="card card--back" aria-label="Card back">
    <div class="brand">
      <h2 class="brand__name">Tamsin Crumbs</h2>
      <p class="brand__tagline">TREATS AND CAKES</p>
    </div>
    <div class="figure" role="img" aria-label="Illustration of a baker in a pink apron holding a tray of cupcakes, cropped at the card edge"></div>
    <div class="contact">
      <p class="contact__name">Tamsin Hollis</p>
      <p class="contact__row">
        <svg viewBox="0 0 30 30" aria-hidden="true">
          <circle cx="15" cy="15" r="13.5" fill="none" stroke="var(--rose)" stroke-width="1.4"/>
          <path d="M10 9.5 l3 -1 l1.6 3.6 l-1.8 1.3 a8 8 0 0 0 3.8 3.8 l1.3 -1.8 l3.6 1.6 l-1 3 c-6 1 -11.5 -4.5 -10.5 -10.5z" fill="none" stroke="var(--rose)" stroke-width="1.3" stroke-linejoin="round"/>
        </svg>
        <span>555.014.0237</span>
      </p>
      <p class="contact__row">
        <svg viewBox="0 0 30 30" aria-hidden="true">
          <circle cx="15" cy="15" r="13.5" fill="none" stroke="var(--rose)" stroke-width="1.4"/>
          <rect x="8" y="10" width="14" height="10" fill="none" stroke="var(--rose)" stroke-width="1.3"/>
          <path d="M8 10 l7 6 l7 -6 M8 20 l5 -5 M22 20 l-5 -5" fill="none" stroke="var(--rose)" stroke-width="1.3"/>
        </svg>
        <span>TamsinHollisBakes@postmix.com</span>
      </p>
    </div>
  </section>

  <p class="side-label side-label--front">FRONT</p>
  <p class="side-label side-label--back">BACK</p>
</main>
</body>
</html>
```